Brochure to advertise our unique physiotherapy clinic to general practitioners

We want to advertise our unique physiotherapy clinic to general practitioners (GPs) to develop there awareness of both our existence and services offered. The brochure should highlight our uniqueness (i.e. providing the highest quality care, advice and education) based on our expert research-based knowledge and skills. After reading the brochure, we want GPs to feel like they know us a little and feel happy to refer their patients to our clinic.
Attached is a draft flyer containing our logo, contact details, profile pictures and the information we would like to be contained in the brochure. We would like the brochure to be A4 double sided and able to be folded to fit into an envelope. More material (pictures) and understanding of our clinic can be found at www.kinetreva.com.au

A brief background of our team:
Our team currently consists of two physiotherapists specialising in the management of musculoskeletal and sports injuries, Dr Howard Tenniscombe and Dr Lionel Fairweather. Both Howard and Lionel have completed PhDs related to musculosketal injury management, and continue to be actively involved in international research groups. Between them they have authored more than 50 peer reviewed papers, presented at countless national and international conferences, and coordinate numerous courses to facilitate professional development of other clinicians. Most importantly, they continue to enjoy mixing these research and teaching activities with treating patients.

Updates
Project Deadline Extended
Reason: Consultation with clinic partner is needed and to allow time for modifications and additional designs. We will pick one, just want quality.
Thanks

Project Deadline Extended

Thank you for some great designs thus far everyone. We have decided to remove the fees from the brochure so please do the same for any future submissions. In the process of trying to provide feedback now.
Thanks
Project Deadline Extended
Reason: A couple of designs are close and we want to allow time to make appropriate modifications. This will be the last extension. Thanks for everyones effort so far

Project Deadline Extended

Target Market(s)
Australian General Practitioners and other health professionals are the targeted audience
Industry/Entity Type
Clinic
Look and feel

```html
<!DOCTYPE html>
<html lang="en">
<head>
<meta charset="utf-8">
<title>Kinetreva Brochure</title>
<link rel="stylesheet" href="https://fonts.googleapis.com/css2?family=Open+Sans:wght@300;400;600;700&display=swap">
<style>
  :root {
    --page-bg: #e9e9eb;
    --paper: #ffffff;
    --ink: #1f1f1f;
    --ink-soft: #4a4a4a;
    --brand-grey: #6b6e72;
    --blue: #1f9bd7;
    --green: #5fb540;
    --lime: #9cc43c;
    --rule: #8a8a8a;
    --navy: #1e2a5a;
  }
  * { box-sizing: border-box; margin: 0; padding: 0; }
  html, body { width: 1200px; height: 793px; overflow: hidden; }
  body { background: var(--page-bg); font-family: "Open Sans", Arial, sans-serif; color: var(--ink); }

  .brochure {
    position: absolute; left: 40px; top: 20px;
    width: 1120px; height: 753px;
    background: var(--paper);
    box-shadow: 0 4px 18px rgba(0,0,0,.18);
    overflow: hidden;
  }

  .hero {
    position: absolute; left: 0; top: 0; width: 100%; height: 330px;
    background: linear-gradient(100deg, #f4f5f7 0%, #dfe3e8 35%, #c9cdd3 58%, #eef0f3 70%, #3b7fd0 82%, #1f5fb8 100%);
    border-bottom: 6px solid var(--blue);
  }
  .hero-brand { position: absolute; left: 42px; top: 155px; }
  .brand { display: flex; align-items: center; gap: 8px; }
  .brand-dot { width: 26px; height: 26px; border-radius: 50%; background: var(--blue); }
  .brand-name { font-weight: 600; font-size: 26px; color: var(--brand-grey); letter-spacing: -.3px; }
  .hero-url { margin-top: 22px; font-size: 12px; color: var(--brand-grey); letter-spacing: .2px; }

  .columns { position: absolute; left: 0; top: 336px; width: 100%; height: 417px; display: flex; }
  .panel { position: relative; width: 33.333%; padding: 18px 26px 0 26px; }
  .panel::after { content: ""; position: absolute; left: 0; right: 0; bottom: 0; height: 14px; }
  .panel--team::after { background: var(--blue); }
  .panel--services::after { background: var(--green); }
  .panel--injuries::after { background: var(--lime); }

  .panel-title { font-weight: 300; font-size: 24px; line-height: 1.05; text-transform: uppercase; color: var(--ink); margin-bottom: 10px; }
  .body-copy { font-size: 10.5px; line-height: 1.45; color: var(--ink); }
  .body-copy strong { font-weight: 700; text-transform: uppercase; }
  .body-copy + .body-copy { margin-top: 12px; }

  .divider { border: 0; border-top: 1px solid var(--rule); margin: 9px 0 10px; }

  .team { display: flex; gap: 40px; padding-left: 8px; }
  .member { text-align: center; }
  .portrait {
    width: 96px; height: 106px; margin: 0 auto; border-radius: 10px;
    background: linear-gradient(180deg, #c9c3bd 0%, #8f857d 60%, #2d3550 100%);
    box-shadow: 0 2px 6px rgba(0,0,0,.35);
  }
  .member:nth-child(2) .portrait { background: linear-gradient(180deg, #eceae6 0%, #c9a78b 55%, #f4f4f4 100%); }
  .member-name { margin-top: 8px; font-size: 10px; color: var(--ink); }

  .services-brand { position: absolute; left: 0; right: 0; bottom: 34px; display: flex; justify-content: center; }
  .services-brand .brand-dot { width: 20px; height: 20px; }
  .services-brand .brand-name { font-size: 18px; }

  .injury-list { display: grid; grid-template-columns: 1fr 1.2fr; column-gap: 8px; margin-top: 12px; }
  .injury-list ul { list-style: none; }
  .injury-list li { font-size: 9px; line-height: 1.3; padding: 4px 0; color: var(--ink); }
  .injury-list li::before { content: "• "; }

  .claims { display: flex; justify-content: space-between; align-items: center; }
  .claims-badge { display: block; }
  .claims-note { margin-top: 8px; font-size: 10.5px; color: var(--navy); padding-left: 24px; }
  .claims-note em { font-weight: 700; }
  .claims-photo {
    width: 110px; height: 72px;
    background: linear-gradient(135deg, #d7dde4 0%, #9aa6b3 45%, #e2e4e8 100%);
  }
</style>
</head>
<body>
<main class="brochure">
  <section class="hero" role="img" aria-label="Photograph of a man training on an elliptical machine in a bright gym, blue sneaker sole in the foreground">
    <div class="hero-brand">
      <div class="brand"><span class="brand-dot"></span><span class="brand-name">Kinetreva</span></div>
      <p class="hero-url">www.kinetreva.com.au</p>
    </div>
  </section>

  <div class="columns">
    <section class="panel panel--team">
      <h2 class="panel-title">Who are we?</h2>
      <p class="body-copy"><strong>Our team</strong> currently consists of two physiotherapists specialising in the management of musculoskeletal and sports injuries, Dr Howard Tenniscombe and Dr Lionel Fairweather. Both Howard and Lionel have completed PhDs related to musculoskeletal injury management, and continue to be actively involved in international research groups. Between them they have authored more than 40 peer reviewed papers, presented at countless national and international conferences, and coordinate numerous courses to facilitate professional development of other clinicians. Most importantly, they continue to enjoy mixing these research and teaching activities with treating patients.</p>
      <hr class="divider">
      <div class="team">
        <figure class="member">
          <div class="portrait" role="img" aria-label="Portrait photograph of Dr Howard Tenniscombe"></div>
          <figcaption class="member-name">Dr Howard Tenniscombe</figcaption>
        </figure>
        <figure class="member">
          <div class="portrait" role="img" aria-label="Portrait photograph of Dr Lionel Fairweather"></div>
          <figcaption class="member-name">Dr Lionel Fairweather</figcaption>
        </figure>
      </div>
    </section>

    <section class="panel panel--services">
      <h2 class="panel-title">Services offered</h2>
      <p class="body-copy"><strong>All patients receive the highest quality</strong> 1-1 physiotherapy treatment and we offer patients accurate, realistic and lasting solution to their problems. We can guarantee the quality of our treatment because we are genuine experts in managing difficult injuries, with a wealth of clinical and research experience. This ultimately means we can more effective care, saving patients both time and money.</p>
      <p class="body-copy"><strong>We have the facilities, knowledge and skills</strong> to complete comprehensive biomechanical assessments, evidence based exercise prescription, access to a full gym, highly effective manual therapy techniques, dry needling, diagnostic ultrasound, shockwave therapy, and foot orthoses advice/prescription. Put together, this will ensure all patients who attend our clinic an optimal recovery from almost any musculoskeletal injury, whether acute or chronic.</p>
      <div class="services-brand">
        <div class="brand"><span class="brand-dot"></span><span class="brand-name">Kinetreva</span></div>
      </div>
    </section>

    <section class="panel panel--injuries">
      <h2 class="panel-title">We treat injuries<br>others cannot fix</h2>
      <p class="body-copy">We have a reputation for successfully managing injuries that are difficult, or unresolving, including:</p>
      <div class="injury-list">
        <ul>
          <li>Achilles tendinopathy</li>
          <li>Patellar tendinopathy</li>
          <li>Tennis elbow</li>
          <li>Rotator cuff injury</li>
          <li>Hamstring origin tendinopathy</li>
          <li>Tibialis posterior tendon injury</li>
          <li>Plantar fasciitis</li>
          <li>Iliotibial band syndrome</li>
        </ul>
        <ul>
          <li>Patellofemoral joint injury</li>
          <li>Back and neck pain</li>
          <li>Chronic strains and sprains</li>
          <li>Shoulder pain</li>
          <li>Groin pain</li>
          <li>Hip impingement</li>
          <li>Stress fractures</li>
          <li>Shin splints (exercise induced leg pain)</li>
        </ul>
      </div>
      <hr class="divider">
      <div class="claims">
        <div>
          <svg class="claims-badge" width="180" height="22" viewBox="0 0 180 22" aria-hidden="true">
            <rect x="4" y="3" width="172" height="16" rx="8" fill="none" stroke="var(--navy)" stroke-width="2"/>
          </svg>
          <p class="claims-note"><em>Fast</em> claims... on the spot</p>
        </div>
        <div class="claims-photo" role="img" aria-label="Photograph of a physiotherapist performing a diagnostic ultrasound on a patient"></div>
      </div>
    </section>
  </div>
</main>
</body>
</html>
```